WP website design (N Kentucky)

We need a wordpress design that will incorporate a professional color scheme with company logo in a clean layout. The design needs to consider that this will be developed on a responsive theme. Colors are undetermined - can use a dark red - logo is black so creative use of colors will be important. Client wants a 'modern' look.
Updates

Project Deadline Extended
Reason: Client wants a few more designs

Industry/Entity Type

It Company

Font styles to use
Serif
Sans Serif

Requirements
Must have
• Must Have:
- Navigation: 1) Home 2) Auctions 3) Auction Marketing 4) Buying at Auction 5) About Us 6) Contact Us

Site will have a slideshow element and the following widgets: 1) Featured Auctions 2) Testimonials blog widget 3) 'Auction Alerts' email sign up 4) Fz Chirpa Zelnix+ icons. Colors can be the meadowline7 gold/black from http://www.brambleridgehouses.example/

In the footer, there will be smaller company logo, the affiliations logo, and contact info below:
Copperfield Gavel Sales, LLC / Wes Pellham
email: wespell@mailbox.example; wes.pellham@ml7.example
phone: (859) 555-0147 mobile phone: (859)555-0182
Domain: http://www.copperfieldgavelsales.example/
Nice to have
• - - Site will have drop-down menus - please indicate the styling, for instance the dropdown menus 1) Upcoming Auctions 2) Past Auctions under the 'Auctions' link

```html
<!DOCTYPE html>
<html lang="en">
<head>
<meta charset="utf-8">
<title>Copperfield Gavel Sales</title>
<link href="https://fonts.googleapis.com/css2?family=Open+Sans:ital,wght@0,400;0,600;0,700;0,800;1,400;1,600&family=Arimo:ital@0;1&display=swap" rel="stylesheet">
<style>
:root{
  --red:#8e0f07;
  --red-bright:#c8231a;
  --ink:#1a1a1a;
  --text:#555;
  --grey-bg:#efefef;
  --panel:#ebebeb;
  --black:#0a0a0a;
  --bar:#141414;
}
*{box-sizing:border-box;margin:0;padding:0}
html,body{width:899px;height:1200px;overflow:hidden;background:#fff}
body{position:relative;font-family:"Open Sans",sans-serif;color:var(--ink)}

.site-header{position:absolute;left:0;top:0;width:899px;height:75px;background:var(--grey-bg);border-top:3px solid var(--red)}
.brand{position:absolute;left:90px;top:10px;width:150px}
.brand-name{display:flex;align-items:center;gap:7px;font-weight:700;font-size:13px;line-height:14px;color:var(--ink)}
.brand-name .mark{width:12px;height:12px;background:var(--ink);flex:none}
.brand-tag{font-size:9px;color:var(--ink);margin-top:14px;letter-spacing:.3px}
.callus{position:absolute;left:542px;top:30px;display:flex;align-items:center;gap:8px;font-size:10px}
.callus .num{color:var(--red)}

.main-nav{position:absolute;left:0;top:75px;width:899px;height:34px;background:var(--red)}
.main-nav a{position:absolute;top:9px;color:#fff;font-size:11px;text-decoration:none}

.hero{position:absolute;left:90px;top:119px;width:719px;height:271px;box-shadow:0 12px 14px -10px rgba(0,0,0,.45)}
.hero-photo{position:absolute;left:0;top:0;width:459px;height:271px;background:linear-gradient(135deg,#d7dcd6 0%,#b9c2b8 35%,#8b4a2c 50%,#c9cfc7 70%,#e3e6e1 100%)}
.hero-panel{position:absolute;left:459px;top:0;width:260px;height:271px;background:var(--black);color:#fff;padding:18px 12px 0 13px}
.hero-panel h1{font-size:26px;font-weight:600;line-height:28px;letter-spacing:-.5px}
.hero-panel h1 span{display:block;font-weight:400}
.hero-panel p{font-size:9px;font-weight:600;line-height:17px;margin-top:22px}
.btn-more{position:absolute;left:14px;top:216px;width:159px;height:28px;background:var(--red);color:#fff;font-size:9.5px;line-height:28px;text-align:center}
.dots{position:absolute;left:19px;top:258px;display:flex;gap:2px}
.dots i{width:6px;height:6px;border-radius:50%;background:#888}
.dots i:first-child{background:#fff}

.tile{position:absolute;top:426px;width:171px;height:141px;background:linear-gradient(160deg,#6a6a6a,#1d1d1d 70%)}
.tile .lbl{position:absolute;left:0;background:var(--red);color:#fff;font-size:10.5px;font-weight:600;height:19px;line-height:19px;padding:0 11px}
.tile .l1{top:88px}
.tile .l2{top:111px}

.feature{position:absolute;top:582px;width:236px}
.feature .ph{height:116px}
.feature h3{font-size:11px;font-weight:400;color:var(--red);margin-top:12px}
.feature p{font-size:8.7px;line-height:14px;color:var(--text);margin-top:4px}
.feature .more{display:block;text-align:right;font-size:8.5px;font-style:italic;color:var(--red);margin-top:9px}

.alerts{position:absolute;left:611px;top:595px;width:198px;height:193px;background:linear-gradient(150deg,#e6e6e6,#b5b5b5 60%,#d2d2d2);border:1px solid #bbb;padding:12px 0 0 26px}
.alerts h2{font-size:25px;font-weight:800;line-height:30px;color:#111;letter-spacing:.3px}
.alerts h2 span{display:block;color:var(--red-bright)}
.alerts .label{font-size:13px;margin-top:13px;color:#222}
.alerts .field{width:163px;height:23px;background:#050505;color:#ccc;font-size:9.5px;line-height:23px;padding-left:7px;margin-top:7px}
.alerts .submit{width:62px;height:21px;background:var(--red);color:#fff;font-size:9.5px;line-height:21px;text-align:center;margin-top:7px;border:1px solid #5a0803}

.blog-title{position:absolute;left:90px;top:811px;font-size:11px;font-weight:600;color:var(--red)}
.blog-arrows{position:absolute;left:784px;top:818px;display:flex;gap:1px}
.blog-arrows span{width:11px;height:11px;background:var(--red-bright);color:#fff;font-size:8px;line-height:11px;text-align:center}
.post{position:absolute;top:838px;width:109px}
.post .ph{height:75px;background:linear-gradient(160deg,#6e5a4c,#2a2220)}
.post p{font-size:8.7px;line-height:11px;color:var(--text);margin-top:7px}
.post .date{font-size:7.6px;font-style:italic;font-weight:600;color:var(--red-bright);margin-top:4px}

.testimonial{position:absolute;left:90px;top:974px;width:718px;height:107px;background:var(--panel)}
.testimonial .ph{position:absolute;left:18px;top:16px;width:74px;height:81px;background:linear-gradient(160deg,#d9cabd,#6b5344)}
.testimonial blockquote{position:absolute;left:125px;top:20px;width:580px;font-family:"Arimo",sans-serif;font-style:italic;font-size:13.5px;line-height:23px;color:#999}
.testimonial .q{color:#e6a13a;font-size:11px;vertical-align:top}
.testimonial cite{font-style:normal;font-size:10.5px;color:#333;margin-left:24px}
.testimonial .more{position:absolute;left:127px;top:81px;font-size:10.5px;font-weight:600;color:#444}

.site-footer{position:absolute;left:0;top:1094px;width:899px;height:77px;background:var(--red)}
.footer-info{position:absolute;left:90px;top:10px;font-size:9px;line-height:14.3px;color:#fff;white-space:nowrap}
.badge{position:absolute;background:#1a1a1a}
.footer-logo{position:absolute;left:663px;top:11px;width:145px;height:55px;background:#fff;border:1px solid #999;display:flex;flex-direction:column;justify-content:center;padding-left:10px}
.footer-logo .brand-name{font-size:10px;line-height:11px;gap:5px}
.footer-logo .brand-name .mark{width:9px;height:9px}
.footer-logo .brand-tag{font-size:6.5px;margin-top:5px}

.bottom-bar{position:absolute;left:0;top:1171px;width:899px;height:29px;background:var(--bar)}
.bottom-bar small{position:absolute;left:90px;top:9px;font-size:8.5px;color:#888}
.social{position:absolute;left:724px;top:7px;display:flex;gap:4px}
.social span{width:15px;height:15px;border-radius:50%;background:#e8e8e8}
</style>
</head>
<body>

<header class="site-header">
  <div class="brand">
    <div class="brand-name"><span class="mark"></span>Copperfield Gavel Sales</div>
    <div class="brand-tag">Wes Pellham, Auctioneer</div>
  </div>
  <div class="callus">
    <svg width="22" height="22" viewBox="0 0 22 22" aria-hidden="true"><circle cx="11" cy="11" r="10" fill="none" stroke="#222" stroke-width="1.2"/><path d="M8 6c-1 1-1.5 2.5-.5 5s3 4.5 4.5 5c1 .3 2-.2 2.5-1l-1.5-2-1.5.8c-1-.5-2.3-2-2.6-3.2l1.3-1L9 6z" fill="#222"/></svg>
    <span>Call Us</span><span class="num">(859) 555-0147 &nbsp;/&nbsp; (859)555-0182</span>
  </div>
</header>

<nav class="main-nav">
  <a style="left:91px">Home</a>
  <a style="left:186px">Auctions</a>
  <a style="left:297px">Auction Marketing</a>
  <a style="left:454px">Buying at Auction</a>
  <a style="left:606px">About Us</a>
  <a style="left:717px">Contact Us</a>
</nav>

<section class="hero">
  <div class="hero-photo" role="img" aria-label="Wooden auction gavel resting on banknotes"></div>
  <div class="hero-panel">
    <h1>Copperfield Gavel<span>Sales</span></h1>
    <p>Lorem ipsum dolor sit amet, consectetur adipiscing elit, sed do eiusmod tempor incididunt ut labore et dolore magna aliqua. Ut enim ad minim veniam, quis nostrud exercitation ullamco laboris nisi ut aliquip ex ea commodo consequat.</p>
    <div class="btn-more">CLICK HERE FOR MORE INFO</div>
    <div class="dots"><i></i><i></i><i></i><i></i></div>
  </div>
</section>

<div class="tile" style="left:90px" role="img" aria-label="Crowd at an auction with a raised hand">
  <span class="lbl l1">ABOUT</span><span class="lbl l2">COPPERFIELD GAVEL SALES</span>
</div>
<div class="tile" style="left:271px" role="img" aria-label="Gavel in motion">
  <span class="lbl l1">AUCTION</span><span class="lbl l2">MARKETING</span>
</div>
<div class="tile" style="left:453px" role="img" aria-label="Bidder holding a numbered paddle">
  <span class="lbl l1">BUYING</span><span class="lbl l2">AT AUCTION</span>
</div>
<div class="tile" style="left:637px" role="img" aria-label="Auctioneer at a podium before an audience">
  <span class="lbl l1">FEATURED</span><span class="lbl l2">AUCTIONS</span>
</div>

<article class="feature" style="left:90px">
  <div class="ph" role="img" aria-label="Auctioneer calling bids with a microphone" style="background:linear-gradient(120deg,#c9a06a,#e8d7c2 45%,#b5462f 90%)"></div>
  <h3>Lorem ipsum</h3>
  <p>Lorem ipsum dolor sit amet, consectetur adipiscing elit, sed do eiusmod tempor incididunt ut labore et dolore magna aliqua.</p>
  <span class="more">Learn more...</span>
</article>
<article class="feature" style="left:356px">
  <div class="ph" role="img" aria-label="Golden gavel on a dark red background" style="background:linear-gradient(160deg,#6b0d0a,#3a0604 60%,#8a1410)"></div>
  <h3>Lorem ipsum</h3>
  <p>Lorem ipsum dolor sit amet, consectetur adipiscing elit, sed do eiusmod tempor incididunt ut labore et dolore magna aliqua.</p>
  <span class="more">Learn more...</span>
</article>

<aside class="alerts">
  <h2>AUCTION<span>ALERTS</span></h2>
  <div class="label">Email sign up</div>
  <div class="field">Enter your email address</div>
  <div class="submit">Submit</div>
</aside>

<h2 class="blog-title">LATEST BLOG</h2>
<div class="blog-arrows"><span>&lsaquo;</span><span>&rsaquo;</span></div>

<div class="post" style="left:90px"><div class="ph" role="img" aria-label="Auction crowd with bid paddle"></div><p>Lorem ipsum dolor sit am consectetur</p><div class="date">Posted on 22 march 2014</div></div>
<div class="post" style="left:214px"><div class="ph" role="img" aria-label="Bidders raising hands"></div><p>Lorem ipsum dolor sit am consectetur</p><div class="date">Posted on 22 march 2014</div></div>
<div class="post" style="left:335px"><div class="ph" role="img" aria-label="Bidder holding up a number card"></div><p>Lorem ipsum dolor sit am consectetur</p><div class="date">Posted on 22 march 2014</div></div>
<div class="post" style="left:455px"><div class="ph" role="img" aria-label="Banquet hall auction event"></div><p>Lorem ipsum dolor sit am consectetur</p><div class="date">Posted on 22 march 2014</div></div>
<div class="post" style="left:578px"><div class="ph" role="img" aria-label="Man holding a bid paddle"></div><p>Lorem ipsum dolor sit am consectetur</p><div class="date">Posted on 22 march 2014</div></div>
<div class="post" style="left:700px"><div class="ph" role="img" aria-label="Audience in an auction hall" style="background:linear-gradient(160deg,#4a5060,#1d1f26)"></div><p>Lorem ipsum dolor sit am consectetur</p><div class="date">Posted on 22 march 2014</div></div>

<section class="testimonial">
  <div class="ph" role="img" aria-label="Portrait of a smiling client"></div>
  <blockquote><span class="q">&ldquo;</span> Lorem ipsum dolor sit amet, consectetur adipisicing elit, sed do eiusmod tempor incididunt ut labore et dolore magna aliqua. <span class="q">&rdquo;</span><cite>-Rhea Talbot, Signal Harbor</cite></blockquote>
  <div class="more">More Testimonials &rarr;</div>
</section>

<footer class="site-footer">
  <div class="footer-info">
    Copperfield Gavel Sales, LLC / Wes Pellham<br>
    email: wespell@mailbox.example; wes.pellham@ml7.example<br>
    phone: (859) 555-0147 mobile phone: (859)555-0182<br>
    Domain: http://www.copperfieldgavelsales.example/
  </div>
  <div class="badge" style="left:396px;top:17px;width:38px;height:47px" role="img" aria-label="Auctioneer association badge"></div>
  <div class="badge" style="left:448px;top:22px;width:76px;height:36px;border-radius:4px" role="img" aria-label="Certified specialist badge"></div>
  <div class="badge" style="left:538px;top:18px;width:84px;height:44px;border-radius:50%" role="img" aria-label="State auctioneers association badge"></div>
  <div class="footer-logo">
    <div class="brand-name"><span class="mark"></span>Copperfield Gavel Sales</div>
    <div class="brand-tag">Wes Pellham, Auctioneer</div>
  </div>
</footer>

<div class="bottom-bar">
  <small>copyright 2014</small>
  <div class="social"><span aria-label="Fz"></span><span aria-label="Chirpa"></span><span aria-label="Zelnix+"></span><span aria-label="Photo sharing"></span></div>
</div>

</body>
</html>
```